依頼概要
■ 依頼の目的/概要
飲食店で毎月誕生日月に顧客リストにあるお客様に誕生日DMをお送りする。

■ 重視する点/検討基準
シンプルかつ幅広い客層にマッチ。
1年間通して使用するため、季節感がないもの。
ハッピバースディが伝わるもの。
割引券1000円、ケーキプレゼントがわかるもの。
(添付のDMにある条件。昨年使用したものです)

■ 利用用途
誕生日DM

■ その他/注意点
当社運営ブランド全店共通DMのため、ブランドロゴを
下のほうに表示します。

■ 選んだ理由

デザインが社内で一致

■ 提案者全員のお礼・コメント

昨年より反応が期待できそうです。ありがとうございました。

```html
<!DOCTYPE html>
<html lang="ja">
<head>
<meta charset="UTF-8">
<title>お誕生日DM</title>
<link href="https://fonts.googleapis.com/css2?family=Noto+Sans+JP:wght@500;700;900&family=Noto+Serif+JP:wght@500;700;900&display=swap" rel="stylesheet">
<style>
  :root{
    --gold-light:#f4e7b8;
    --gold:#c9a54e;
    --gold-dark:#8f6f22;
    --ink:#1a1a1a;
    --red:#d7141e;
    --yellow:#ffe600;
    --paper:#ffffff;
    --rule:#b9a36a;
  }
  *{margin:0;padding:0;box-sizing:border-box}
  html,body{width:813px;height:1200px;overflow:hidden;background:var(--paper)}
  .card{
    position:relative;width:813px;height:1200px;
    background:linear-gradient(135deg,var(--gold-dark) 0%,var(--gold-light) 25%,var(--gold) 50%,var(--gold-light) 75%,var(--gold-dark) 100%);
    font-family:"Noto Sans JP",sans-serif;color:var(--ink);
  }
  .card__inner{position:absolute;inset:20px;background:var(--paper)}
  .headline{
    position:absolute;top:28px;left:0;right:0;text-align:center;
    font-weight:900;font-size:62px;line-height:70px;letter-spacing:2px;
  }
  .lead{
    position:absolute;top:170px;left:0;right:0;text-align:center;
    font-family:"Noto Serif JP",serif;font-weight:700;font-size:23px;
  }
  .brands{
    position:absolute;top:222px;left:0;right:0;display:flex;justify-content:center;gap:34px;
  }
  .brand{
    display:flex;align-items:center;gap:8px;
    font-family:"Noto Serif JP",serif;font-weight:900;font-size:30px;color:var(--ink);
  }
  .brand__mark{width:22px;height:22px;background:var(--ink)}
  .brand__mark--round{border-radius:50%}
  .divider{position:absolute;left:22px;right:22px;height:2px;background:var(--rule)}
  .badge{
    position:absolute;width:58px;height:58px;border-radius:50%;background:var(--red);color:#fff;
    display:flex;align-items:center;justify-content:center;font-weight:900;font-size:17px;
  }
  .offer-one__label{
    position:absolute;top:395px;left:100px;font-weight:700;font-size:27px;display:flex;align-items:center;gap:14px;
  }
  .offer-one__brands{font-size:13px;font-family:"Noto Serif JP",serif;font-weight:900;letter-spacing:1px}
  .voucher{
    position:absolute;top:450px;left:100px;right:40px;height:102px;background:var(--yellow);
    display:flex;align-items:baseline;justify-content:center;font-family:"Noto Serif JP",serif;font-weight:900;
  }
  .voucher__amount{font-size:96px;line-height:102px;letter-spacing:2px}
  .voucher__unit{font-size:46px}
  .voucher__note{position:absolute;top:556px;left:0;right:0;text-align:center;font-weight:700;font-size:15px;padding-left:60px}
  .offer-two{
    position:absolute;top:590px;left:40px;right:40px;height:300px;border:2px solid var(--rule);
  }
  .offer-two__title{position:absolute;top:18px;left:82px;font-weight:700;font-size:28px;color:var(--red)}
  .reserve{
    position:absolute;top:-6px;right:14px;width:44px;height:106px;background:var(--red);color:#fff;
    writing-mode:vertical-rl;text-align:center;font-weight:900;font-size:26px;line-height:44px;
  }
  .cake{
    position:absolute;top:90px;left:14px;width:200px;height:190px;border-radius:10px;
    background:radial-gradient(circle at 50% 60%,#f7e2c4 0%,#f2c7a2 45%,#fbefe2 100%);
  }
  .offer-two__body{
    position:absolute;top:110px;left:232px;right:24px;font-size:18px;line-height:31px;font-weight:500;
  }
  .notes{
    position:absolute;top:905px;left:40px;right:40px;display:grid;grid-template-columns:1fr 1fr;column-gap:18px;
  }
  .notes li{
    list-style:none;font-size:15px;line-height:20px;padding:11px 0;border-bottom:1px solid var(--rule);font-weight:500;
  }
  .notes li::before{content:"■";margin-right:2px}
</style>
</head>
<body>
<div class="card">
  <div class="card__inner">
    <h1 class="headline">お誕生日<br>おめでとうございます</h1>
    <p class="lead">私たちのお店で思い出に残る時間を過ごしませんか?</p>
    <div class="brands">
      <span class="brand"><span class="brand__mark"></span>炭火亭</span>
      <span class="brand"><span class="brand__mark brand__mark--round"></span>いろり庵</span>
      <span class="brand"><span class="brand__mark brand__mark--round"></span>鍋まる</span>
    </div>
    <div class="divider" style="top:352px"></div>

    <div class="badge" style="top:390px;left:30px">その1</div>
    <p class="offer-one__label">全店共通お食事優待券 <span class="offer-one__brands">炭火亭・いろり庵・鍋まる</span></p>
    <div class="voucher"><span class="voucher__amount">1,000</span><span class="voucher__unit">円券</span></div>
    <p class="voucher__note">有効期限:お誕生日月の1ヶ月間</p>

    <section class="offer-two">
      <div class="badge" style="top:10px;left:10px">その2</div>
      <h2 class="offer-two__title">お誕生日ケーキプレゼント</h2>
      <div class="reserve">予約制</div>
      <div class="cake" role="img" aria-label="誕生日ケーキの写真"></div>
      <p class="offer-two__body">ご希望の方にはご利用日の3日前までにご予約頂ければケーキ(1人前)をプレゼントいたします。[平日限定]ご家族・友人や恋人とのお祝いの場に是非ご利用ください。</p>
    </section>

    <ul class="notes">
      <li>ご注文時にこのハガキをご提示ください。</li>
      <li>期間中1回のみ上記特典をご利用いただけます。</li>
      <li>1組様1枚のみご利用となります。</li>
      <li>1組様3,000円以上のお会計でご利用いただけます。</li>
      <li>他のサービスとの併用はできません。</li>
      <li>上記記載店舗のみでご利用いただけます。</li>
    </ul>
  </div>
</div>
</body>
</html>
```